Craft brewery website - 7 Harbors Brewery

Looking for a simple site similar to fennwaldbrew.com or tallridgeales.com with the following features:
- incorporates existing logo (file attached)
- has a consistent look and feel throughout the site that works in harmony with the logo. Please suggest a cool font to use!
- incorporates all or some of the attached images
- has the following tabs/pages: home, our story, brews, blog, contact.
- has some sort of prominent image/design under the top menu bar that can be updated with content - so a placeholder for text. Please use this text on home page: "we brew up our passion for honest ingredients, our curiosity for different cultures, and social and environmental consciousness into characteristic beers." And "Beers with a Twist for the good of the world, for the fun of the party"
- has a scrolling set of images under main section that will list beers. Please create five placeholders for beers: Weizenbock, Copper Lantern, Stout, Saison, Rusty Marlow

Brewery

1 page

• Looking for a simple site similar to fennwaldbrew.com with the following features:
• - incorporates existing logo (file attached)
• - has a consistent look and feel throughout the site that works in harmony with the logo. Please suggest a cool font to use!
• - incorporates all or some of the attached images
• - has the following tabs/pages: home, our story, brews, blog, contact.
• - has some sort of prominent image/design under the top menu bar that can be updated with content - so a placeholder for text. Please use this text on home page: "we brew up our passion for honest ingredients, our curiosity for different cultures, and social and environmental consciousness into characteristic beers." And "Beers with a Twist for the good of the world, for the fun of the party"
• - has a scrolling set of images under main section that will list beers. Please create five placeholders for beers: Weizenbock, Copper Lantern, Stout, Saison, Rusty Marlow

```html
<!DOCTYPE html>
<html lang="en">
<head>
<meta charset="utf-8">
<title>7 Harbors Brewery</title>
<link href="https://fonts.googleapis.com/css2?family=Oswald:wght@500;700&family=Open+Sans:wght@400;600;700&display=swap" rel="stylesheet">
<style>
:root{
  --gold:#c9962d;
  --gold-light:#dcae4e;
  --gold-deep:#9d6f1c;
  --ink:#1c1815;
  --wood:#3b2a1e;
  --wood-dark:#24190f;
  --cream:#f5efe3;
  --white:#ffffff;
  --text:#5a5148;
  --muted:#8a8178;
}
*{box-sizing:border-box;margin:0;padding:0}
html,body{width:1200px;height:3860px;overflow:hidden}
body{font-family:"Open Sans",Arial,sans-serif;color:var(--text);background:var(--white);position:relative}
.heading{font-family:"Oswald",Impact,sans-serif;font-weight:700;text-transform:uppercase;letter-spacing:2px}
.btn{display:inline-block;font-family:"Oswald",Impact,sans-serif;font-weight:500;font-size:15px;letter-spacing:1px;text-transform:uppercase;padding:9px 20px;background:var(--ink);color:var(--white)}
.circle-icon{display:inline-block;width:26px;height:26px;border-radius:50%;background:var(--gold);vertical-align:middle;margin-left:6px}

/* top bar */
.top-bar{height:40px;background:var(--ink);color:var(--white);display:flex;justify-content:space-between;align-items:center;padding:0 50px;font-size:15px}
.top-bar .phone{display:flex;align-items:center;gap:8px}

/* nav */
.nav{position:absolute;top:40px;left:0;width:1200px;height:62px;background:linear-gradient(var(--gold-light),var(--gold));display:flex;align-items:center;padding:0 50px;z-index:3}
.nav ul{list-style:none;display:flex;justify-content:space-between;width:100%}
.nav li{font-family:"Oswald",Impact,sans-serif;font-size:19px;color:var(--white);text-transform:uppercase;letter-spacing:1px}
.nav .gap{width:220px}
.logo{position:absolute;left:520px;top:30px;width:160px;height:160px;border-radius:50%;background:var(--white);border:6px solid var(--ink);display:flex;align-items:center;justify-content:center;text-align:center;z-index:4}
.logo span{font-family:"Oswald",Impact,sans-serif;font-weight:700;font-size:24px;line-height:1.1;color:var(--ink);text-transform:uppercase}

/* hero */
.hero{position:absolute;top:102px;left:0;width:1200px;height:598px;background:radial-gradient(circle at 50% 50%,#5b4632,#1d150e 75%)}
.hero-frame{position:absolute;left:270px;top:120px;width:680px;height:440px;display:grid;grid-template-columns:repeat(6,1fr);grid-template-rows:repeat(4,1fr);gap:8px;border:3px solid var(--white);padding:8px}
.tile{background:linear-gradient(135deg,#c8b79b,#7a5d3b);border:2px solid var(--white)}
.tile.amber{background:linear-gradient(135deg,#f1c04f,#a06a12)}
.tile.blue{background:linear-gradient(135deg,#2e4b8c,#16254a)}
.hero-text{grid-column:2/6;grid-row:1/3;background:rgba(28,24,21,.85);display:flex;align-items:center;justify-content:center;text-align:center;color:var(--white);font-family:"Oswald",Impact,sans-serif;font-weight:700;font-size:28px;line-height:1.3;padding:10px}

/* our beer */
.our-beer{position:absolute;top:700px;left:0;width:1200px;height:600px;background:repeating-linear-gradient(90deg,var(--wood) 0 58px,var(--wood-dark) 58px 62px);color:var(--white);text-align:center}
.our-beer h2{font-size:46px;margin-top:48px;color:var(--white)}
.our-beer p{width:1000px;margin:14px auto 0;font-size:14px;line-height:1.6;color:#e6dccb}
.beer-row{display:flex;gap:28px;margin:40px 44px 0}
.beer-card{width:200px;height:330px;border:5px solid var(--gold);background:var(--cream);display:flex;flex-direction:column}
.beer-photo{flex:1;margin:10px;background:linear-gradient(#f7f2e8,#d8cdb8)}
.beer-name{height:48px;background:var(--wood-dark);color:var(--gold-light);font-family:"Oswald",Impact,sans-serif;font-weight:700;font-size:18px;text-transform:uppercase;display:flex;align-items:center;justify-content:center;letter-spacing:1px}

/* about */
.about{position:absolute;top:1300px;left:0;width:1200px;height:420px;background:linear-gradient(var(--gold-light),var(--gold));text-align:center;color:var(--white)}
.about h2{font-size:44px;margin-top:52px}
.about p{width:1060px;margin:18px auto 0;font-size:14px;line-height:1.6}
.about .btn{margin-top:26px}

/* brewery */
.brewery{position:absolute;top:1720px;left:0;width:1200px;height:640px;background:linear-gradient(90deg,#1f160f,#3b2a1c)}
.brewery-photo{position:absolute;right:0;top:30px;width:720px;height:610px;background:radial-gradient(circle at 55% 55%,#e0a53a,#7b4a1c 45%,#2a1c12 80%)}
.brewery-copy{position:absolute;left:60px;top:90px;width:420px;color:var(--white)}
.brewery-copy h2{font-size:42px}
.brewery-copy p{font-size:14px;line-height:1.65;margin-top:14px;color:#e6dccb}
.brewery-copy .btn{background:var(--gold);margin-top:24px}

/* blog */
.blog{position:absolute;top:2360px;left:0;width:1200px;height:500px;background:var(--white);text-align:center}
.blog h2{font-size:44px;color:#1d2a66;margin-top:44px}
.card-row{display:flex;gap:30px;margin:34px 80px 0;text-align:left}
.blog-card{width:237px}
.blog-photo{height:180px;border:4px solid #d9d3c9;background:linear-gradient(135deg,#d18a3a,#4a2c1a)}
.blog-date{position:absolute;width:46px;height:52px;background:var(--gold);color:var(--white);font-family:"Oswald",Impact,sans-serif;font-size:14px;text-align:center;line-height:1.3;padding-top:6px}
.blog-card h3{font-family:"Oswald",Impact,sans-serif;font-size:17px;color:var(--ink);text-transform:uppercase;margin-top:12px}
.blog-card p{font-size:13px;line-height:1.5;color:var(--muted);margin-top:6px}
.read-more{font-size:13px;font-weight:700;color:var(--ink);margin-top:8px;display:block}
.arrow{position:absolute;top:250px;width:28px;height:44px}

/* products */
.products{position:absolute;top:2860px;left:0;width:1200px;height:440px;background:linear-gradient(#b9862a,#d4a445);text-align:center}
.products h2{font-size:44px;color:var(--white);margin-top:40px}
.product-card{width:237px;text-align:center}
.product-photo{height:170px;background:var(--white);border:4px solid var(--cream);display:flex;align-items:center;justify-content:center}
.product-photo div{width:120px;height:120px;border-radius:8px;background:linear-gradient(#5b6a7a,#2b3440)}
.product-card h3{font-family:"Oswald",Impact,sans-serif;font-size:17px;color:var(--white);text-transform:uppercase;margin-top:12px}
.price{font-size:14px;font-weight:700;color:var(--ink);margin-top:2px}
.view{font-size:13px;font-weight:700;color:var(--white);margin-top:4px;display:block}

/* inquiry */
.inquiry{position:absolute;top:3300px;left:0;width:1200px;height:260px;background:var(--white)}
.inquiry h2{text-align:center;font-size:40px;color:var(--ink);margin-top:26px;display:flex;align-items:center;justify-content:center;gap:14px}
.fields{display:flex;gap:24px;margin:26px 50px 0}
.field{flex:1;height:44px;border:1px solid #cfc8bd;font-size:14px;color:var(--muted);padding:12px 14px}
.fields.second .field{flex:none;width:818px}
.submit{height:44px;width:100px;background:var(--ink);color:var(--white);font-family:"Oswald",Impact,sans-serif;font-size:16px;text-transform:uppercase;display:flex;align-items:center;justify-content:center}

/* footer */
.footer{position:absolute;top:3560px;left:0;width:1200px;height:300px;background:var(--ink);color:#d8d0c4;font-size:14px}
.footer-contact{position:absolute;left:50px;top:40px;line-height:1.6}
.contact-line{display:flex;gap:10px;align-items:flex-start;margin-bottom:6px}
.footer-phone{position:absolute;left:250px;top:40px;line-height:2}
.footer-logo{position:absolute;left:530px;top:20px;width:140px;height:140px;border-radius:50%;background:var(--white);border:5px solid var(--gold);display:flex;align-items:center;justify-content:center;text-align:center}
.footer-logo span{font-family:"Oswald",Impact,sans-serif;font-weight:700;font-size:20px;color:var(--ink);text-transform:uppercase;line-height:1.1}
.newsletter{position:absolute;left:780px;top:40px;width:370px}
.newsletter h4{font-family:"Oswald",Impact,sans-serif;color:var(--white);font-size:18px;text-transform:uppercase}
.signup{display:flex;margin-top:14px}
.signup div:first-child{flex:1;height:40px;background:var(--white);color:var(--muted);padding:10px 12px;font-size:13px}
.signup div:last-child{width:110px;background:var(--gold);color:var(--white);font-family:"Oswald",Impact,sans-serif;text-transform:uppercase;display:flex;align-items:center;justify-content:center}
.footer-rule{position:absolute;left:50px;right:50px;top:196px;border-top:1px solid #3a332d}
.footer-links{position:absolute;left:50px;top:214px;display:flex;gap:22px;color:var(--white)}
.copyright{position:absolute;left:50px;top:246px;font-size:13px;color:var(--muted)}
.follow{position:absolute;right:50px;top:214px;text-align:right;font-family:"Oswald",Impact,sans-serif;color:var(--white);text-transform:uppercase;font-size:17px}
.follow div{margin-top:8px}
.base{position:absolute;bottom:0;left:0;width:1200px;height:10px;background:var(--gold)}
</style>
</head>
<body>

<header>
  <div class="top-bar">
    <div>Follow Us <span class="circle-icon"></span><span class="circle-icon"></span><span class="circle-icon"></span></div>
    <div class="phone">
      <svg width="18" height="18" viewBox="0 0 24 24"><path fill="#dcae4e" d="M6.6 10.8a15 15 0 0 0 6.6 6.6l2.2-2.2c.3-.3.7-.4 1-.2 1.1.4 2.3.6 3.6.6.6 0 1 .4 1 1V20c0 .6-.4 1-1 1A17 17 0 0 1 3 4c0-.6.4-1 1-1h3.5c.6 0 1 .4 1 1 0 1.3.2 2.5.6 3.6.1.3 0 .7-.2 1z"/></svg>
      (03) 5550 2147
    </div>
  </div>
  <nav class="nav">
    <ul>
      <li>Home</li><li>Our Story</li><li>Brews</li><li class="gap"></li><li>Blog</li><li>Shop</li><li>Contact Us</li>
    </ul>
  </nav>
  <div class="logo"><span>7 Harbors<br>Brewery</span></div>
</header>

<section class="hero" role="img" aria-label="Dark brewery taproom photograph behind a collage of beer photos">
  <div class="hero-frame">
    <div class="tile"></div>
    <div class="hero-text">Beers With A Twist For The Good of The World For The Fun of The Party</div>
    <div class="tile amber"></div>
    <div class="tile amber"></div>
    <div class="tile blue"></div>
    <div class="tile"></div>
    <div class="tile amber"></div>
    <div class="tile"></div>
    <div class="tile blue"></div>
    <div class="tile amber"></div>
    <div class="tile"></div>
    <div class="tile"></div>
    <div class="tile amber"></div>
    <div class="tile blue"></div>
    <div class="tile"></div>
    <div class="tile amber"></div>
  </div>
</section>

<section class="our-beer">
  <h2 class="heading">Our Beer</h2>
  <p>Lorem ipsum dolor sit amet, consectetuer adipiscing elit, sed diam nonummy nibh euismod tincidunt ut laoreet dolore magna aliquam erat volutpat. Ut wisi enim ad minim veniam, quis nostrud exerci tation ullamcorper suscipit lobortis nisl ut aliquip ex ea commodo.</p>
  <div class="beer-row">
    <div class="beer-card"><div class="beer-photo" role="img" aria-label="Weizenbock bottle"></div><div class="beer-name">Weizenbock</div></div>
    <div class="beer-card"><div class="beer-photo" role="img" aria-label="Copper Lantern bottle"></div><div class="beer-name">Copper Lantern</div></div>
    <div class="beer-card"><div class="beer-photo" role="img" aria-label="Stout bottle"></div><div class="beer-name">Stout</div></div>
    <div class="beer-card"><div class="beer-photo" role="img" aria-label="Saison bottle"></div><div class="beer-name">Saison</div></div>
    <div class="beer-card"><div class="beer-photo" role="img" aria-label="Rusty Marlow bottle"></div><div class="beer-name">Rusty Marlow</div></div>
  </div>
</section>

<section class="about">
  <h2 class="heading">About 7 Harbors Brewery</h2>
  <p>Lorem ipsum dolor sit amet, consectetuer adipiscing elit, sed diam nonummy nibh euismod tincidunt ut laoreet dolore magna aliquam erat volutpat. Ut wisi enim ad minim veniam, quis nostrud exerci tation ullamcorper suscipit lobortis nisl ut aliquip ex ea commodo consequat. Duis autem vel eum iriure dolor in hendrerit in vulputate velit esse molestie consequat, vel illum dolore eu feugiat nulla facilisis at vero eros et accumsan et iusto odio dignissim qui blandit praesent luptatum zzril delenit augue duis dolore te feugait nulla facilisi.</p>
  <span class="btn">Read More &rsaquo;</span>
</section>

<section class="brewery">
  <div class="brewery-photo" role="img" aria-label="Glasses of beer, bottles and an oak barrel on a wooden table"></div>
  <div class="brewery-copy">
    <h2 class="heading">Our Brewery</h2>
    <p>Lorem ipsum dolor sit amet, consectetuer adipiscing elit, sed diam nonummy nibh euismod tincidunt ut laoreet dolore magna aliquam erat volutpat. Ut wisi enim ad minim veniam, quis nostrud exerci tation ullamcorper suscipit lobortis nisl ut aliquip ex ea commodo consequat.</p>
    <span class="btn">Read More &rsaquo;</span>
  </div>
</section>

<section class="blog">
  <h2 class="heading">Latest Blog Posts</h2>
  <svg class="arrow" style="left:30px" viewBox="0 0 28 44"><path d="M22 4 6 22l16 18" fill="none" stroke="#9a948c" stroke-width="4"/></svg>
  <svg class="arrow" style="right:30px" viewBox="0 0 28 44"><path d="M6 4l16 18L6 40" fill="none" stroke="#9a948c" stroke-width="4"/></svg>
  <div class="card-row">
    <article class="blog-card"><div class="blog-date">15<br>Jul</div><div class="blog-photo" role="img" aria-label="Friends toasting at the brewery"></div><h3>Lorem Ipsum Dolor Sit</h3><p>Lorem ipsum dolor sit amet, consectetuer adipiscing elit, sed diam nonummy.</p><span class="read-more">Read More &rsaquo;</span></article>
    <article class="blog-card"><div class="blog-date">15<br>Jul</div><div class="blog-photo" role="img" aria-label="Row of beer glasses"></div><h3>Lorem Ipsum Dolor Sit</h3><p>Lorem ipsum dolor sit amet, consectetuer adipiscing elit, sed diam nonummy.</p><span class="read-more">Read More &rsaquo;</span></article>
    <article class="blog-card"><div class="blog-date">15<br>Jul</div><div class="blog-photo" role="img" aria-label="Crowd at a brewery party"></div><h3>Lorem Ipsum Dolor Sit</h3><p>Lorem ipsum dolor sit amet, consectetuer adipiscing elit, sed diam nonummy.</p><span class="read-more">Read More &rsaquo;</span></article>
    <article class="blog-card"><div class="blog-date">15<br>Jul</div><div class="blog-photo" role="img" aria-label="Tasting flight of beers on a bar"></div><h3>Lorem Ipsum Dolor Sit</h3><p>Lorem ipsum dolor sit amet, consectetuer adipiscing elit, sed diam nonummy.</p><span class="read-more">Read More &rsaquo;</span></article>
  </div>
</section>

<section class="products">
  <h2 class="heading">Featured Products</h2>
  <svg class="arrow" style="left:30px;top:200px" viewBox="0 0 28 44"><path d="M22 4 6 22l16 18" fill="none" stroke="#ffffff" stroke-width="4"/></svg>
  <svg class="arrow" style="right:30px;top:200px" viewBox="0 0 28 44"><path d="M6 4l16 18L6 40" fill="none" stroke="#ffffff" stroke-width="4"/></svg>
  <div class="card-row">
    <div class="product-card"><div class="product-photo" role="img" aria-label="Blue brewery t-shirt"><div></div></div><h3>Mens Tee Fat Large</h3><div class="price">$45.00</div><span class="view">View Product &rsaquo;</span></div>
    <div class="product-card"><div class="product-photo" role="img" aria-label="Black pint cup"><div></div></div><h3>Cup Black Large</h3><div class="price">$20.00</div><span class="view">View Product &rsaquo;</span></div>
    <div class="product-card"><div class="product-photo" role="img" aria-label="Black cap"><div></div></div><h3>Harbor Cap Hat</h3><div class="price">$30.00</div><span class="view">View Product &rsaquo;</span></div>
    <div class="product-card"><div class="product-photo" role="img" aria-label="Grey hoodie"><div></div></div><h3>Driftwood Hoodie</h3><div class="price">$50.00</div><span class="view">View Product &rsaquo;</span></div>
  </div>
</section>

<section class="inquiry">
  <h2 class="heading">
    <svg width="34" height="34" viewBox="0 0 24 24"><rect x="2" y="5" width="20" height="14" rx="1" fill="#1d2a66"/><path d="M2 6l10 7 10-7" fill="none" stroke="#fff" stroke-width="1.6"/></svg>
    Quick Inquiry
  </h2>
  <div class="fields">
    <div class="field">First Name</div><div class="field">Last Name</div><div class="field">Email</div><div class="field">Phone</div>
  </div>
  <div class="fields second">
    <div class="field">Message</div><div class="submit">Submit &rsaquo;</div>
  </div>
</section>

<footer class="footer">
  <div class="footer-contact">
    <div class="contact-line">
      <svg width="16" height="20" viewBox="0 0 16 20"><path d="M8 0a7 7 0 0 0-7 7c0 5 7 13 7 13s7-8 7-13a7 7 0 0 0-7-7zm0 10a3 3 0 1 1 0-6 3 3 0 0 1 0 6z" fill="#c9962d"/></svg>
      <span>Lorem ipsum dolor sit<br>amet, consectetuer<br>adipiscing elit, sed</span>
    </div>
  </div>
  <div class="footer-phone">
    <div class="contact-line"><svg width="16" height="16" viewBox="0 0 24 24"><path fill="#c9962d" d="M6.6 10.8a15 15 0 0 0 6.6 6.6l2.2-2.2c.3-.3.7-.4 1-.2 1.1.4 2.3.6 3.6.6.6 0 1 .4 1 1V20c0 .6-.4 1-1 1A17 17 0 0 1 3 4c0-.6.4-1 1-1h3.5c.6 0 1 .4 1 1 0 1.3.2 2.5.6 3.6.1.3 0 .7-.2 1z"/></svg>(03) 5550 2147</div>
    <div class="contact-line"><svg width="16" height="16" viewBox="0 0 24 24"><rect x="2" y="5" width="20" height="14" fill="#c9962d"/><path d="M2 6l10 7 10-7" fill="none" stroke="#1c1815" stroke-width="1.6"/></svg>hello@7harborsbrewery.com</div>
  </div>
  <div class="footer-logo"><span>7 Harbors<br>Brewery</span></div>
  <div class="newsletter">
    <h4>Newsletter Signup</h4>
    <div class="signup"><div>Enter your email here</div><div>Subscribe</div></div>
  </div>
  <div class="footer-rule"></div>
  <div class="footer-links"><span>Home</span><span>Our Story</span><span>Brews</span><span>Blog</span><span>Shop</span><span>Contact Us</span></div>
  <div class="copyright">Copyright &copy; 2017 7 Harbors Brewery | All Rights Reserved.</div>
  <div class="follow">Follow Us<div><span class="circle-icon"></span><span class="circle-icon"></span><span class="circle-icon"></span></div></div>
  <div class="base"></div>
</footer>

</body>
</html>
```